Business Card Design Project

We are an agricultural business based in Brisbane.
We design, manage and operate regional saleyards. Our logo is green/silver in colour and details of our business can be found on our website www.tovrak.com.au

Just wanting a corporate design for some business cards and include name, position, contact details.

Thanks

```html
<!DOCTYPE html>
<html lang="en">
<head>
<meta charset="utf-8">
<title>Tovrak – Business Card</title>
<link rel="stylesheet" href="https://fonts.googleapis.com/css2?family=Tinos:wght@700&display=swap">
<style>
  :root {
    --backdrop: #a1a1a1;
    --green-top: #2a8a2a;
    --green-mid: #237023;
    --charcoal: #3b3b3b;
    --edge: #1c5e1c;
    --arrow-fill: #a1a1a1;
    --arrow-shade: #3a3a3a;
    --ink: #ffffff;
    --photo-tone-a: #c9c2b8;
    --photo-tone-b: #8d8a86;
  }
  html, body {
    margin: 0;
    padding: 0;
    width: 1200px;
    height: 781px;
    overflow: hidden;
    background: var(--backdrop);
  }
  .card-canvas {
    display: block;
    width: 1200px;
    height: 781px;
  }
  .card-text {
    font-family: "Tinos", "Times New Roman", serif;
    font-weight: 700;
    fill: var(--ink);
  }
  .position-title { font-size: 35px; }
  .brand-name { font-size: 54px; letter-spacing: 4px; }
  .contact-phone { font-size: 28px; }
  .contact-email { font-size: 25px; }
</style>
</head>
<body>
<svg class="card-canvas" viewBox="0 0 1200 781" xmlns="http://www.w3.org/2000/svg">
  <defs>
    <linearGradient id="panelGradient" x1="0" y1="0" x2="0" y2="1">
      <stop offset="0" stop-color="var(--green-top)"/>
      <stop offset="0.45" stop-color="var(--green-mid)"/>
      <stop offset="1" stop-color="var(--charcoal)"/>
    </linearGradient>
    <linearGradient id="photoGradient" x1="0" y1="0" x2="0" y2="1">
      <stop offset="0" stop-color="var(--photo-tone-a)"/>
      <stop offset="1" stop-color="var(--photo-tone-b)"/>
    </linearGradient>
    <filter id="cardShadow" x="-5%" y="-5%" width="110%" height="115%">
      <feDropShadow dx="2" dy="4" stdDeviation="3" flood-color="#000" flood-opacity="0.45"/>
    </filter>
    <filter id="textShadow" x="-5%" y="-30%" width="110%" height="160%">
      <feDropShadow dx="2" dy="2" stdDeviation="1.2" flood-color="#000" flood-opacity="0.95"/>
    </filter>
    <filter id="insetShade" x="-5%" y="-5%" width="110%" height="110%">
      <feDropShadow dx="-3" dy="3" stdDeviation="2.5" flood-color="var(--arrow-shade)" flood-opacity="0.8"/>
    </filter>
  </defs>

  <!-- Card panels -->
  <g class="card-panels" filter="url(#cardShadow)">
    <rect class="panel-left" x="108" y="144" width="489" height="493" fill="url(#panelGradient)" stroke="var(--edge)" stroke-width="2"/>
    <rect class="panel-right" x="601" y="144" width="490" height="493" fill="url(#panelGradient)" stroke="var(--edge)" stroke-width="2"/>
  </g>

  <!-- Directional arrows -->
  <g class="direction-arrows" filter="url(#insetShade)">
    <polygon class="arrow-left" points="198,390 513,234 513,547" fill="var(--arrow-fill)"/>
    <polygon class="arrow-right" points="687,234 997,390 687,547" fill="var(--arrow-fill)"/>
  </g>

  <!-- Position title -->
  <text class="card-text position-title" x="150" y="207" textLength="925" lengthAdjust="spacing" filter="url(#textShadow)">GENERAL MANAGER-TVX PORTFOLIO</text>

  <!-- Company name -->
  <text class="card-text brand-name" x="600" y="358" text-anchor="middle">TOVRAK</text>

  <!-- Portrait -->
  <rect class="portrait-frame" x="546" y="398" width="110" height="136" fill="#111"/>
  <rect class="portrait" x="549" y="401" width="104" height="130" fill="url(#photoGradient)" role="img" aria-label="Portrait photograph of the general manager"/>

  <!-- Contact details -->
  <text class="card-text contact-phone" x="466" y="579" textLength="264" lengthAdjust="spacing" filter="url(#textShadow)">Mob: 0400 118 275</text>
  <text class="card-text contact-email" x="378" y="614" textLength="416" lengthAdjust="spacing" filter="url(#textShadow)">marcus@tovrak.com.au</text>
</svg>
</body>
</html>
```